依頼詳細
イラスト(写真枠なし)、写真枠入りのデザインを依頼します。
用途は2015年の年賀状用です。

1つのデザインに対して使用できる写真の枚数枠は1枚~5枚です。
タテ型1点もしくはヨコ型1点でご提案下さい。
(提案されるデザインがイラストタイプなのか、写真入りタイプなのか、また写真枠の数についてはお任せいたします。)

デザインを作成するにあたって

・ユーザーは子供の写真や家族関係が多いです。
・写真が主役なのでその点を考慮の上、デザイン下さい。
・定番のタイプから家族向けのやさしいタイプのものまで幅広く、募集します。

複数採用予定ですので同じ方でも複数のデザインを提案して頂いても構いません。
こちらの希望に合致しましたデザイナー様は今後も別途、ご依頼させて頂ければと考えております。
デザインのテンプレートの作成仕様及びPSDの雛形については添付ファイルを参照して下さい。

添付資料を必ず、読んでください。
添付資料の条件から外れたデザインにつきましては、どんなに良いデザインでも採用できません(システム上)のでご注意下さい。
記載項目
はがきサイズ

詳細は添付資料でご確認下さい。
補足でデザインの外枠部分にデザインがかかる場合は裁ち落とし時にカットされるおそれがございます。
デザインがカットされない様に余白にしたり、塗り足し等で調整して下さい。
その点を考慮して、デザイン作成して下さい。
希望イメージ
シンプル 複雑
単色 カラフル
暗い 明るい
日常 高級
遊び心 厳粛
未来的 伝統的
女性的 男性的
希望する色
特にありませんが明るめの感じでお願いします。
納品ファイル
• フォトショップ形式 (.psd)
補足説明
デザインはオリジナルの物のみとします。(同じデザインの色違い等の提案もOKです。)
採用作品デザインの使用・販売に関する権利は弊社のものとさせて頂き、弊社での商用利用に使用させて頂きます。
契約が成立した場合でも盗作等が発覚した場合や他でも同じデザインが使用されている等が発覚した場合は契約を破棄させて頂きます。

添付資料の住所枠(サイズも含めて)については必須でお願いしますが挨拶文枠は設けて頂かなくても構いません。

また今回は1点だけでなく計1~100点の募集となります。
契約成立の金額は下記金額となります。
全応募デザインより弊社にてランク付けさせて頂き、上位1位の方には5万円、以下1万円〜500円迄の報酬となります。
※デザインのクオリティーや弊社の希望に沿わないデザインが多い場合は上記の募集以下での採用になる場合がございます。
予め、ご了承下さい。

1位 5万円
2~5位 1万円
6~10位 5千円
11~50位 1000円
51~100位 500円
ご連絡が遅れてすみません。
この度は多数の素敵なデザインを作成頂きまして誠にありがとうございます。
現在、弊社スタッフで選定及び順位付け作業を行っております。
今週中には作業完了予定です。
当選の連絡につきましては週末及び週明けまでにご連絡させて頂きますので今、暫くお待ち頂ければ幸いです。
以上、ご連絡申し上げます。
■ 選んだ理由

たくさんのデザイナー様から素敵なデザインを提案頂きましたが社内で色々と検討した結果、こちらのデザインをトップに選定させて頂く事になりました。
理由はかわいらしさもありながら正月っぽいデザインが気に入りました。

■ 提案者全員のお礼・コメント

この度は多数の素敵なデザインを作成頂きまして誠にありがとうございました。
お陰様で複数の採用をさせて頂きました。
別途、選定させて頂いたデザイナー様には連絡をさせて頂いておりますので、もしよろしければ使用させて頂ければ幸いです。
改めて御礼申し上げます。

```html
<!DOCTYPE html>
<html lang="ja">
<head>
<meta charset="utf-8">
<title>2015 年賀状 写真5枚</title>
<link rel="stylesheet" href="https://fonts.googleapis.com/css2?family=Noto+Sans+JP:wght@400;500&family=Noto+Serif+JP:wght@300;400&display=swap">
<style>
  :root {
    --frame: #1e7f6d;
    --field: #2ba58d;
    --paper: #ffffff;
    --ink: #f4fbf8;
    --soft: #cfeee6;
    --tag: #6b4a2f;
    --sheep: #f1f4ef;
  }
  html, body { margin: 0; padding: 0; overflow: hidden; }
  body { width: 804px; height: 1200px; background: var(--frame); }
  .card {
    position: relative; width: 804px; height: 1200px; box-sizing: border-box;
    border: 18px solid var(--frame); background: var(--field); overflow: hidden;
    font-family: "Noto Sans JP", sans-serif; color: var(--ink);
  }
  .photo {
    position: absolute; left: 96px; width: 148px; height: 182px;
    background: var(--paper);
  }
  .sheep {
    position: absolute; background: var(--sheep); border-radius: 45% 50% 45% 50%;
    opacity: .95;
  }
  .year-tag {
    position: absolute; left: 584px; top: 48px; width: 64px; height: 26px;
    background: var(--tag); color: var(--paper); border-radius: 3px;
    font-size: 15px; font-weight: 500; text-align: center; line-height: 26px;
    transform: rotate(-10deg); letter-spacing: 2px;
  }
  .greeting {
    position: absolute; left: 610px; top: 62px; margin: 0;
    writing-mode: vertical-rl; font-family: "Noto Serif JP", serif;
    font-weight: 300; font-size: 68px; line-height: 80px;
    letter-spacing: 64px; color: var(--ink);
  }
  .message {
    position: absolute; left: 540px; top: 116px; width: 56px; height: 528px; margin: 0;
    writing-mode: vertical-rl; font-size: 22px; line-height: 28px;
    letter-spacing: 0; color: var(--ink); overflow: hidden;
  }
  .sender { position: absolute; left: 362px; top: 662px; font-size: 13px; line-height: 23px; }
  .sender p { margin: 0; }
  .families { position: absolute; left: 362px; top: 842px; font-size: 16px; }
  .family-row { display: flex; align-items: flex-end; height: 46px; }
  .family-row .surname { width: 89px; }
  .family-row .person { width: 107px; }
  .family-row .dot { width: 41px; text-align: center; }
  ruby rt { font-size: 8px; color: var(--soft); }
  .contact { position: absolute; left: 362px; top: 1064px; font-size: 13px; line-height: 24px; }
  .contact p { margin: 0; }
</style>
</head>
<body>
<main class="card">
  <div class="photo" style="top:30px"></div>
  <div class="photo" style="top:262px"></div>
  <div class="photo" style="top:490px"></div>
  <div class="photo" style="top:718px"></div>
  <div class="photo" style="top:946px"></div>

  <div class="sheep" role="img" aria-label="草原の羊のイラスト" style="left:335px;top:148px;width:60px;height:40px"></div>
  <div class="sheep" role="img" aria-label="草原の羊のイラスト" style="left:385px;top:312px;width:64px;height:44px"></div>
  <div class="sheep" role="img" aria-label="草原の羊のイラスト" style="left:434px;top:618px;width:60px;height:42px"></div>
  <div class="sheep" role="img" aria-label="草原の羊のイラスト" style="left:18px;top:740px;width:62px;height:44px"></div>
  <div class="sheep" role="img" aria-label="草原の羊のイラスト" style="left:690px;top:1110px;width:62px;height:44px"></div>

  <div class="year-tag">2015</div>
  <h1 class="greeting">謹賀新年</h1>

  <p class="message">○○○○○○○○○○○○○○○○○○○○○○○○○○○○○○○○○○○○○○</p>

  <div class="sender">
    <p>〒000-0000</p>
    <p>東京都○○区○○町 xxxx-xxxx-xxxx</p>
    <p>○○○○○○○○○マンション xxxx-xxxx</p>
    <p>○○○○○○○○○○○○○○</p>
    <p>株式会社○○○○○○○○ ○○支店</p>
    <p>○○○○部署</p>
  </div>

  <div class="families">
    <div class="family-row">
      <span class="surname"><ruby>年頭<rt>ねんとう</rt></ruby></span>
      <span class="person"><ruby>太郎<rt>たろう</rt></ruby> (xx)</span>
      <span class="dot">・</span>
      <span class="person"><ruby>花子<rt>はなこ</rt></ruby> (xx)</span>
    </div>
    <div class="family-row">
      <span class="surname"></span>
      <span class="person"><ruby>一郎<rt>いちろう</rt></ruby> (xx)</span>
      <span class="dot">・</span>
      <span class="person"><ruby>二郎<rt>じろう</rt></ruby> (xx)</span>
    </div>
    <div class="family-row">
      <span class="surname"></span>
      <span class="person"><ruby>三郎<rt>さぶろう</rt></ruby> (xx)</span>
      <span class="dot">・</span>
      <span class="person"><ruby>四郎<rt>しろう</rt></ruby> (xx)</span>
    </div>
  </div>

  <div class="contact">
    <p>電話：000-0000-0000</p>
    <p>FAX：000-0000-0000</p>
    <p>URL：000-0000-0000</p>
  </div>
</main>
</body>
</html>
```